Bread Baking Blog

I need theme modification/customization and logo for a Wordpress theme that I can use the blog about bread baking. Needs to include pictures & recipes.

Can provide access to my pagelumen.com site. Have paid for https://quilvanstore.com/themes/brisk/ but open to alternatives.

The site name is "velmo42.com" (type 85 flour is a type of bread flour used in artisan bread baking). Not particular on color palette - am looking for your creativity.

I've included some logos for other domains I have to help provide some inspiration.

```html
<!DOCTYPE html>
<html lang="en">
<head>
<meta charset="utf-8">
<title>velmo42.com — Bread Baking Blog</title>
<link href="https://fonts.googleapis.com/css2?family=Mulish:wght@400;600;700;800&family=Lobster&display=swap" rel="stylesheet">
<style>
:root{
  --brown:#7e3c0b;
  --brown-dark:#5e2b06;
  --gold:#fcc76b;
  --gold-shadow:rgba(252,199,107,.45);
  --text:#3d3d3d;
  --muted:#666;
  --light:#f3f3f3;
  --hero:#ececec;
  --footer:#e9e9e9;
  --line:#cfcfcf;
  --white:#fff;
}
*{box-sizing:border-box;margin:0;padding:0}
html,body{width:1200px;height:3610px;overflow:hidden}
body{position:relative;background:var(--white);font-family:"Mulish",sans-serif;color:var(--text)}
.abs{position:absolute}
.script{font-family:"Lobster",cursive;color:var(--brown);font-weight:400}
.btn{position:absolute;display:flex;align-items:center;justify-content:center;background:var(--gold);color:var(--brown);font-weight:700;font-size:14px;border-radius:20px;text-transform:uppercase;letter-spacing:.2px;box-shadow:0 3px 8px var(--gold-shadow)}

/* header */
.site-header{position:absolute;left:0;top:0;width:1200px;height:100px;background:var(--white)}
.brand{position:absolute;display:flex;align-items:center;justify-content:center;border-radius:50%;background:var(--brown);color:#fbe3b5;font-weight:800;font-size:19px;letter-spacing:0;white-space:nowrap;overflow:hidden}
.nav a{position:absolute;top:38px;font-size:15px;color:#555;text-decoration:none}
.search{position:absolute;left:880px;top:38px}

/* hero */
.hero{position:absolute;left:0;top:100px;width:1200px;height:597px;background:var(--hero)}
.hero-photo{position:absolute;left:631px;top:0;width:569px;height:597px;background:linear-gradient(90deg,var(--hero) 0%,#d9cdbd 18%,#c9a064 45%,#e6b23f 65%,#f0e6d8 100%)}
.hero h1{position:absolute;left:156px;top:201px;font-size:41px;line-height:42px;font-weight:700;color:var(--brown)}
.hero p{position:absolute;left:156px;top:302px;width:420px;font-size:19.5px;line-height:26px;color:var(--text)}

/* recipes */
.section-title{position:absolute;font-size:41px}
.outline-btn{position:absolute;left:871px;top:740px;width:172px;height:37px;border:2px solid var(--brown);border-radius:20px;color:var(--brown);font-size:15px;font-weight:600;display:flex;align-items:center;justify-content:center}
.recipe{position:absolute;top:815px;width:195px;height:222px;overflow:hidden}
.recipe .photo{position:absolute;inset:0}
.recipe .shade{position:absolute;left:0;right:0;bottom:0;height:100px;background:rgba(20,16,12,.78);color:var(--white);text-align:center}
.recipe h3{font-size:16.5px;font-weight:700;margin-top:13px}
.recipe p{font-size:14px;line-height:18px;margin-top:7px}
.recipe .heart{position:absolute;right:12px;top:15px}
.divider{position:absolute;height:1px;background:var(--line)}

/* posts */
.post{position:absolute;left:157px;width:560px;height:240px}
.post .photo{position:absolute;left:0;top:0;width:240px;height:238px}
.post .meta{position:absolute;left:264px;top:7px;font-size:14px;color:var(--brown);font-weight:600}
.post .meta span{margin-left:26px}
.post h2{position:absolute;left:264px;top:36px;width:290px;font-size:22px;line-height:26px;font-weight:500;color:#2d2d2d}
.post p{position:absolute;left:264px;top:98px;width:280px;font-size:14.5px;line-height:18px;color:var(--muted)}
.post .btn{left:264px;top:182px;width:102px;height:32px;font-size:13px}

/* sidebar */
.widget{position:absolute;left:760px;width:276px;background:var(--light)}
.widget-head{height:48px;background:var(--brown);color:var(--white);font-family:"Lobster",cursive;font-size:25px;display:flex;align-items:center;justify-content:center}
.widget .copy{font-size:14.5px;line-height:18px;text-align:center;color:var(--muted)}
.mini{position:absolute;left:26px;width:240px;height:72px}
.mini .thumb{position:absolute;left:0;top:0;width:71px;height:71px}
.mini p{position:absolute;left:80px;top:0;font-size:13px;line-height:16px;color:var(--muted)}
.mini time{position:absolute;left:80px;top:54px;font-size:11.5px;color:#999}
.field{position:absolute;left:26px;width:225px;height:39px;border-radius:20px;background:var(--white);font-size:14.5px;color:#555;padding-left:18px;display:flex;align-items:center}
.promo{position:absolute;left:760px;top:2388px;width:276px;height:287px;background:linear-gradient(180deg,#6e6e6e 0%,#5a5a5a 55%,#9b7447 80%,#4a4a4a 100%)}
.promo h4{position:absolute;left:0;width:276px;top:34px;text-align:center;color:var(--white);font-size:29px;line-height:33px;font-weight:800}

/* pagination */
.page{position:absolute;top:3143px;width:30px;height:29px;background:#e4e4e4;color:#555;font-size:14px;display:flex;align-items:center;justify-content:center}
.page.current{background:var(--gold);color:var(--brown);font-weight:700}

/* footer */
.site-footer{position:absolute;left:0;top:3238px;width:1200px;height:372px;background:var(--footer)}
.site-footer h5{position:absolute;top:61px;font-size:21px;font-weight:700;color:var(--brown)}
.site-footer ul{position:absolute;top:103px;list-style:none;font-size:13.5px;line-height:21.7px;color:#666}
.contact-item{position:absolute;left:837px;display:flex;align-items:flex-start}
.contact-item .ico{width:31px;height:31px;border-radius:50%;background:var(--brown);display:flex;align-items:center;justify-content:center;flex:none}
.contact-item p{margin-left:11px;font-size:13.5px;line-height:18px;color:#666}
.copyright{position:absolute;left:0;width:1200px;top:327px;text-align:center;font-size:16px;color:#444}
</style>
</head>
<body>

<header class="site-header">
  <div class="brand" style="left:144px;top:17px;width:150px;height:150px;z-index:3">velmo42.com</div>
  <nav class="nav">
    <a style="left:388px">Tutorials</a>
    <a style="left:484px">Bread Making</a>
    <a style="left:621px">Reviews</a>
    <a style="left:719px">Blog</a>
    <a style="left:791px">About</a>
  </nav>
  <svg class="search" width="20" height="20" viewBox="0 0 20 20"><circle cx="8" cy="8" r="6" fill="none" stroke="var(--brown)" stroke-width="2.6"/><line x1="12.5" y1="12.5" x2="18" y2="18" stroke="var(--brown)" stroke-width="2.8" stroke-linecap="round"/></svg>
  <div class="btn" style="left:937px;top:31px;width:113px;height:37px;font-size:15px">Recipes</div>
</header>

<section class="hero">
  <div class="hero-photo" role="img" aria-label="Mother and daughter in yellow aprons kneading dough together in a bright kitchen"></div>
  <h1>Sed ut perspiciande<br>volup tatac cusantium</h1>
  <p>At vero eos et accusamus et iusto odio digni ssimos ducimus qui blanditiis praesentiumv oluptatum deleniti atque corrup</p>
  <div class="btn" style="left:156px;top:406px;width:137px;height:35px;font-size:14.5px">Read More</div>
</section>

<h2 class="section-title script" style="left:157px;top:730px">Recipes</h2>
<div class="outline-btn">VIEW ALL RECIPES</div>

<article class="recipe" style="left:157px"><div class="photo" role="img" aria-label="Smiling baker in a kitchen" style="background:linear-gradient(160deg,#8a8378,#c9a78a 50%,#4b4038)"></div><svg class="heart" width="16" height="14" viewBox="0 0 16 14"><path d="M8 13.5 1.5 7A3.8 3.8 0 0 1 8 2.5 3.8 3.8 0 0 1 14.5 7Z" fill="#fff"/></svg><div class="shade"><h3>Recipe Name</h3><p>Sed ut perspiciatis nde<br>omnis iste natusu</p></div></article>
<article class="recipe" style="left:387px"><div class="photo" role="img" aria-label="Sliced loaf and pretzel on a dark board" style="background:linear-gradient(160deg,#3a3532,#8a6a48 50%,#2b2724)"></div><svg class="heart" width="16" height="14" viewBox="0 0 16 14"><path d="M8 13.5 1.5 7A3.8 3.8 0 0 1 8 2.5 3.8 3.8 0 0 1 14.5 7Z" fill="#fff"/></svg><div class="shade"><h3>Recipe Name</h3><p>Sed ut perspiciatis nde<br>omnis iste natusu</p></div></article>
<article class="recipe" style="left:617px"><div class="photo" role="img" aria-label="Dough ball on a floured table" style="background:linear-gradient(160deg,#6d4f3c,#d8c8b4 50%,#5b3e2c)"></div><svg class="heart" width="16" height="14" viewBox="0 0 16 14"><path d="M8 13.5 1.5 7A3.8 3.8 0 0 1 8 2.5 3.8 3.8 0 0 1 14.5 7Z" fill="#fff"/></svg><div class="shade"><h3>Recipe Name</h3><p>Sed ut perspiciatis nde<br>omnis iste natusu</p></div></article>
<article class="recipe" style="left:847px"><div class="photo" role="img" aria-label="Rustic loaves with rosemary" style="background:linear-gradient(160deg,#3c3f44,#b88c58 50%,#2f3033)"></div><svg class="heart" width="16" height="14" viewBox="0 0 16 14"><path d="M8 13.5 1.5 7A3.8 3.8 0 0 1 8 2.5 3.8 3.8 0 0 1 14.5 7Z" fill="#fff"/></svg><div class="shade"><h3>Recipe Name</h3><p>Sed ut perspiciatis nde<br>omnis iste natusu</p></div></article>

<div class="divider" style="left:182px;top:1094px;width:855px"></div>

<h2 class="section-title script" style="left:157px;top:1132px">Latest Blog</h2>

<article class="post" style="top:1215px"><div class="photo" role="img" aria-label="Dough ball dusted with flour on a wooden table" style="background:radial-gradient(circle at 50% 45%,#e7d6b4 0 22%,#6b3e1f 45%,#3a2413)"></div><div class="meta">October 14, 2020<span>5 Comments</span></div><h2>At vero eosetaccusamuset iusto odio dignissimoc</h2><p>At vero eos et accusamlouet iusto odio dign issimos du cilom us qui blandiitiis praesentium voluptatum deleniti atlue corr upti quos dolores et qualor</p><div class="btn">Read More</div></article>
<article class="post" style="top:1488px"><div class="photo" role="img" aria-label="Grandmother and child baking together" style="background:linear-gradient(135deg,#8c7e6d,#d9c7ae 50%,#6e5c4c)"></div><div class="meta">October 14, 2020<span>5 Comments</span></div><h2>At vero eosetaccusamuset iusto odio dignissimoc</h2><p>At vero eos et accusamlouet iusto odio dign issimos du cilom us qui blandiitiis praesentium voluptatum deleniti atlue corr upti quos dolores et qualor</p><div class="btn">Read More</div></article>
<article class="post" style="top:1761px"><div class="photo" role="img" aria-label="Baker holding a tray of fresh buns by the oven" style="background:linear-gradient(135deg,#9b9590,#c9a271 55%,#6b5848)"></div><div class="meta">October 14, 2020<span>5 Comments</span></div><h2>At vero eosetaccusamuset iusto odio dignissimoc</h2><p>At vero eos et accusamlouet iusto odio dign issimos du cilom us qui blandiitiis praesentium voluptatum deleniti atlue corr upti quos dolores et qualor</p><div class="btn">Read More</div></article>
<article class="post" style="top:2033px"><div class="photo" role="img" aria-label="Golden crusty loaf on parchment" style="background:radial-gradient(circle at 45% 50%,#dba860 0 30%,#7a4b24 60%,#3c2717)"></div><div class="meta">October 14, 2020<span>5 Comments</span></div><h2>At vero eosetaccusamuset iusto odio dignissimoc</h2><p>At vero eos et accusamlouet iusto odio dign issimos du cilom us qui blandiitiis praesentium voluptatum deleniti atlue corr upti quos dolores et qualor</p><div class="btn">Read More</div></article>
<article class="post" style="top:2306px"><div class="photo" role="img" aria-label="Hands sprinkling flour over dough" style="background:linear-gradient(180deg,#1e1e1e,#3a3430 55%,#c9b79a 80%,#4a3424)"></div><div class="meta">October 14, 2020<span>5 Comments</span></div><h2>At vero eosetaccusamuset iusto odio dignissimoc</h2><p>At vero eos et accusamlouet iusto odio dign issimos du cilom us qui blandiitiis praesentium voluptatum deleniti atlue corr upti quos dolores et qualor</p><div class="btn">Read More</div></article>
<article class="post" style="top:2579px"><div class="photo" role="img" aria-label="Hands kneading dough on a floured board" style="background:linear-gradient(135deg,#8a5a3c,#e6d3bf 50%,#b3876a)"></div><div class="meta">October 14, 2020<span>5 Comments</span></div><h2>At vero eosetaccusamuset iusto odio dignissimoc</h2><p>At vero eos et accusamlouet iusto odio dign issimos du cilom us qui blandiitiis praesentium voluptatum deleniti atlue corr upti quos dolores et qualor</p><div class="btn">Read More</div></article>
<article class="post" style="top:2852px"><div class="photo" role="img" aria-label="Baker shaping dough in a cloud of flour" style="background:linear-gradient(135deg,#2a2a2a,#8e8a86 55%,#1e1e1e)"></div><div class="meta">October 14, 2020<span>5 Comments</span></div><h2>At vero eosetaccusamuset iusto odio dignissimoc</h2><p>At vero eos et accusamlouet iusto odio dign issimos du cilom us qui blandiitiis praesentium voluptatum deleniti atlue corr upti quos dolores et qualor</p><div class="btn">Read More</div></article>

<aside>
  <section class="widget" style="top:1140px;height:380px">
    <div class="widget-head">About Us</div>
    <div class="abs" role="img" aria-label="Portrait of the blog author" style="left:79px;top:63px;width:118px;height:118px;border-radius:50%;background:linear-gradient(135deg,#d8d2c8,#3d5560)"></div>
    <div class="abs script" style="left:0;width:276px;top:190px;text-align:center;font-size:24px">Jhsniemsh</div>
    <p class="copy abs" style="left:28px;width:220px;top:230px">At vero eos et accusamuet iusto odio dignissimos du cim us qui blanditiis praesentium voluptatum deleniti atque corr upti quos dolores et quas mole stias excepturi sint occae</p>
  </section>

  <section class="widget" style="top:1548px;height:462px">
    <div class="widget-head">See More Posts</div>
    <div class="mini" style="top:71px"><div class="thumb" role="img" aria-label="Bread loaves" style="background:linear-gradient(135deg,#c58a4d,#6b4326)"></div><p>At vero eos et acsam<br>uet iusto odio dignisim<br>osdu cim uslouio</p><time>October 13, 2020</time></div>
    <div class="mini" style="top:167px"><div class="thumb" role="img" aria-label="Baker at work" style="background:linear-gradient(135deg,#444,#b3a090)"></div><p>At vero eos et acsam<br>uet iusto odio dignisim<br>osdu cim uslouio</p><time>October 13, 2020</time></div>
    <div class="mini" style="top:262px"><div class="thumb" role="img" aria-label="Flour on dough" style="background:linear-gradient(160deg,#2b2b2b,#caa67a)"></div><p>At vero eos et acsam<br>uet iusto odio dignisim<br>osdu cim uslouio</p><time>October 13, 2020</time></div>
    <div class="mini" style="top:359px"><div class="thumb" role="img" aria-label="Baguettes" style="background:linear-gradient(135deg,#e3b66c,#7a4c25)"></div><p>At vero eos et acsam<br>uet iusto odio dignisim<br>osdu cim uslouio</p><time>October 13, 2020</time></div>
  </section>

  <section class="widget" style="top:2036px;height:333px">
    <div class="widget-head">Get more stuff</div>
    <p class="copy abs" style="left:30px;width:216px;top:74px">At vero eos et accusamuet iusto odio dignissimos du cim us qui blanditiis praesent</p>
    <div class="field" style="top:147px">Name:</div>
    <div class="field" style="top:200px">Email:</div>
    <div class="btn" style="left:26px;top:256px;width:225px;height:38px;font-size:14.5px">Sign Up</div>
  </section>

  <section class="promo" role="img" aria-label="Assorted breads and a rolling pin on grey stone">
    <h4>FINIBUSONO<br>RUM ETMRUM</h4>
    <div class="btn" style="left:76px;top:116px;width:124px;height:35px;font-size:14.5px">Read More</div>
  </section>
</aside>

<nav>
  <div class="page current" style="left:157px">1</div>
  <div class="page" style="left:195px">2</div>
  <div class="page" style="left:233px">3</div>
  <div class="page" style="left:270px">4</div>
  <div class="page" style="left:308px">5</div>
  <div class="page" style="left:345px">6</div>
  <div class="page" style="left:383px"><svg width="10" height="12" viewBox="0 0 10 12"><path d="M3 1l5 5-5 5" fill="none" stroke="#666" stroke-width="1.5"/></svg></div>
</nav>

<footer class="site-footer">
  <div class="brand" style="left:144px;top:77px;width:150px;height:150px">velmo42.com</div>
  <h5 style="left:401px">Sitemap</h5>
  <ul style="left:401px"><li>Sed ut peatis</li><li>Eunde omnis iste</li><li>Natus error sitvo</li><li>Eptatem accusa</li><li>Ntium doloremqu</li><li>Kaudantium</li><li>Rtam rem periam</li></ul>
  <h5 style="left:625px">Archives</h5>
  <ul style="left:625px"><li>October 2020</li><li>September 2020</li><li>August 2020</li><li>July 2020</li><li>June 2020</li><li>May 2020</li><li>April 202</li></ul>
  <h5 style="left:837px">Contact</h5>
  <div class="contact-item" style="top:106px"><div class="ico"><svg width="12" height="16" viewBox="0 0 12 16"><path d="M6 0a6 6 0 0 0-6 6c0 4.5 6 10 6 10s6-5.5 6-10a6 6 0 0 0-6-6z" fill="#fff"/><circle cx="6" cy="6" r="2.2" fill="var(--brown)"/></svg></div><p>Sed ut peatisunde omnis<br>iste atus error sitvo</p></div>
  <div class="contact-item" style="top:160px"><div class="ico"><svg width="14" height="14" viewBox="0 0 14 14"><path d="M3 0.5 5.2 3.5 4 5.2c.8 1.8 2.6 3.6 4.8 4.8L10.5 8.8 13.5 11l-1.6 2.5C6 13.5.5 8 .5 2.1Z" fill="#fff"/></svg></div><p>Phone:<br>555 014 2290</p></div>
  <div class="contact-item" style="top:213px"><div class="ico"><svg width="14" height="11" viewBox="0 0 14 11"><rect x="0" y="0" width="14" height="11" rx="1.5" fill="#fff"/><path d="M1 1.5 7 6l6-4.5" fill="none" stroke="var(--brown)" stroke-width="1.4"/></svg></div><p>Email:<br>hello@velmo42.com</p></div>
  <div class="divider" style="left:137px;top:306px;width:926px;background:#c8c8c8"></div>
  <p class="copyright">© 2020 All Rights are reserved. Privacy | Terms of use</p>
</footer>

</body>
</html>
```